The K7 Momentum Collective Website

We have a pitch deck and messaging drafted. Target audience is academic institutions and VC investors that have seed money in start ups.

Need a basic website

Industry/Entity Type

LIfe Science, Diagnostic, medical device.

Coding

Coded - Design and coding required

Number of Pages Required

5+ page

```html
<!DOCTYPE html>
<html lang="en">
<head>
<meta charset="utf-8">
<title>The K7 Momentum Collective</title>
<link href="https://fonts.googleapis.com/css2?family=Roboto:wght@400;500;700;900&display=swap" rel="stylesheet">
<style>
:root{
  --blue:#0a6dc2;
  --blue-dark:#0757a0;
  --grey:#8c8c8c;
  --grey-band:#8e8e8e;
  --text:#555;
  --dark:#222;
  --footer:#2a2a2a;
  --card:#f4f4f4;
}
*{margin:0;padding:0;box-sizing:border-box}
html,body{width:1200px;height:3876px;overflow:hidden}
body{position:relative;font-family:'Roboto',sans-serif;color:var(--dark);background:#fff}
.abs{position:absolute}
.topbar{left:0;top:0;width:1200px;height:42px;background:var(--grey)}
.topbar-blue{left:0;top:0;width:870px;height:42px;background:var(--blue);color:#fff;font-size:14px;display:flex;align-items:center;padding-left:112px;gap:14px}
.topbar-social{left:960px;top:11px;display:flex;gap:18px}
.topbar-social svg{width:20px;height:20px}
.header{left:0;top:42px;width:1200px;height:120px;background:#fff}
.brand{display:flex;align-items:center;gap:10px;color:var(--blue);font-weight:700;font-size:17px;line-height:1.1}
.brand-dot{width:22px;height:22px;border-radius:50%;background:var(--blue)}
.nav{right:110px;top:95px;display:flex;gap:31px;font-size:15px;font-weight:500;color:#222;align-items:center}
.nav .active{color:var(--blue)}
.hero{left:0;top:162px;width:1200px;height:650px;overflow:hidden}
.hero-photo{position:absolute;inset:0;background:
  radial-gradient(ellipse 260px 200px at 140px 260px,rgba(240,200,170,.85),transparent 70%),
  radial-gradient(ellipse 220px 220px at 830px 160px,rgba(215,160,130,.8),transparent 70%),
  radial-gradient(ellipse 300px 200px at 1080px 120px,rgba(250,245,225,.95),transparent 70%),
  radial-gradient(ellipse 260px 160px at 620px 520px,rgba(90,70,60,.55),transparent 70%),
  radial-gradient(ellipse 200px 300px at 340px 330px,rgba(60,60,70,.55),transparent 70%),
  radial-gradient(ellipse 260px 300px at 1000px 400px,rgba(70,80,100,.5),transparent 70%),
  linear-gradient(180deg,#d8cfc2 0%,#c7a58c 45%,#9d7e68 100%)}
.hero-box{left:289px;top:180px;width:623px;height:264px;background:rgba(255,255,255,.72);text-align:center;padding-top:40px}
.hero-box h1{font-size:33px;font-weight:700;color:#222;letter-spacing:.3px}
.hero-box p{font-size:17px;color:#333;line-height:27px;margin:14px auto 0;width:470px}
.btn{display:inline-block;background:var(--blue);color:#fff;font-weight:700;font-size:14px;border-radius:24px;padding:0 24px;height:44px;line-height:44px}
.hero-box .btn{margin-top:20px}
.about-img{left:112px;top:888px;width:444px;height:444px;border-radius:50%;background:var(--blue)}
.about-img div{position:absolute;left:13px;top:0;width:420px;height:420px;border-radius:50%;background:
  radial-gradient(ellipse 90px 110px at 140px 120px,rgba(230,200,180,.7),transparent 70%),
  radial-gradient(ellipse 90px 100px at 250px 190px,rgba(240,235,230,.8),transparent 70%),
  radial-gradient(ellipse 120px 200px at 330px 260px,rgba(20,25,35,.9),transparent 70%),
  radial-gradient(ellipse 110px 160px at 110px 300px,rgba(30,45,80,.9),transparent 70%),
  linear-gradient(150deg,#b9b3ab 0%,#7b7f88 50%,#3b4150 100%)}
.about-text{left:623px;top:918px;width:466px}
.h2{font-size:38px;font-weight:700;letter-spacing:1px}
.h2 .b{color:var(--blue)}.h2 .g{color:var(--grey)}
.about-text p{font-size:14px;color:#666;line-height:25.5px;text-align:justify;margin-top:20px}
.about-text .btn{margin-top:28px}
.solution{left:0;top:1452px;width:1200px;height:485px;background:var(--grey-band)}
.solution h2{position:absolute;top:66px;width:100%;text-align:center;color:#fff;font-size:36px;font-weight:700;letter-spacing:1px}
.sol-card{top:153px;width:232px;height:249px;background:var(--card);box-shadow:0 3px 8px rgba(0,0,0,.2);text-align:center;border:3px solid transparent}
.sol-card.on{border-color:var(--blue);background:#fff}
.sol-card .ic{margin:30px auto 0;width:114px;height:114px;display:block}
.sol-card span{display:block;margin-top:22px;font-size:17px;font-weight:500;line-height:26px;color:#222}
.team-h{left:111px;top:2128px;font-size:36px;font-weight:700;line-height:50px;letter-spacing:1px}
.member{top:2035px;width:226px;height:256px;background:#fff;border:3px solid #eee;box-shadow:0 2px 6px rgba(0,0,0,.15)}
.member.on{border-color:var(--blue)}
.member .ph{position:absolute;inset:0;background:
  radial-gradient(ellipse 60px 80px at 50% 42%,rgba(210,180,160,.9),transparent 72%),
  radial-gradient(ellipse 110px 70px at 50% 100%,rgba(25,25,30,.95),transparent 75%),
  linear-gradient(180deg,#d9d9d9,#a9a9a9)}
.member .tag{position:absolute;left:14px;bottom:-26px;width:190px;height:52px;border-radius:26px;background:#fff;box-shadow:0 2px 6px rgba(0,0,0,.2);text-align:center;line-height:52px;font-size:15px;font-weight:500}
.member.on .tag{background:var(--blue);color:#fff}
.plan{left:0;top:2417px;width:1200px;height:599px;background:linear-gradient(120deg,#0b63b3,#0a70c8 50%,#0659a6)}
.plan h2{position:absolute;top:50px;width:100%;text-align:center;color:#fff;font-size:36px;font-weight:700;letter-spacing:1px}
.plan-card{top:143px;width:305px;height:358px;background:#fff;border-radius:10px;text-align:center;padding:38px 22px 0}
.plan-card .ic{margin:0 auto;width:90px;height:90px;display:block}
.plan-card h3{margin-top:30px;font-size:17px;font-weight:500}
.plan-card p{margin-top:18px;font-size:15px;line-height:25.5px;color:#777}
.dots{top:538px;left:570px;display:flex;gap:9px}
.dots i{width:7px;height:7px;border-radius:50%;background:rgba(255,255,255,.5)}
.dots i.on{background:#fff}
.touch-h{top:3098px;width:1200px;text-align:center}
.field{height:49px;background:#fff;box-shadow:0 2px 8px rgba(0,0,0,.12);font-size:14px;color:#666;padding:18px 17px 0}
.footer{left:0;top:3540px;width:1200px;height:336px;background:var(--footer);color:#fff}
.footer .brand{position:absolute;left:505px;top:78px;color:var(--blue)}
.fnav{position:absolute;top:143px;width:100%;display:flex;justify-content:center;gap:24px;font-size:19px;font-weight:700}
.fcontact{position:absolute;top:181px;width:100%;text-align:center;font-size:16px}
.fsocial{position:absolute;top:218px;left:524px;display:flex;gap:6px}
.fsocial svg{width:33px;height:33px}
.fline{position:absolute;top:290px;left:111px;width:978px;height:1px;background:#555}
.fcopy{position:absolute;top:306px;width:100%;text-align:center;font-size:12px}
</style>
</head>
<body>

<div class="abs topbar"></div>
<div class="abs topbar-blue">
  <svg width="13" height="13" viewBox="0 0 24 24"><path fill="#b5d3f0" d="M6.6 10.8a15 15 0 006.6 6.6l2.2-2.2c.3-.3.7-.4 1-.2 1.1.4 2.3.6 3.6.6.6 0 1 .4 1 1V20c0 .6-.4 1-1 1A17 17 0 013 4c0-.6.4-1 1-1h3.5c.6 0 1 .4 1 1 0 1.3.2 2.5.6 3.6.1.3 0 .7-.2 1z"/></svg>
  <span>+1 (555) 014 7720</span><span>|</span>
  <svg width="14" height="11" viewBox="0 0 24 18"><rect width="24" height="18" rx="2" fill="#b5d3f0"/><path d="M1 2l11 8 11-8" stroke="#0a6dc2" stroke-width="2" fill="none"/></svg>
  <span>hello@k7momentumcollective.com</span>
</div>
<div class="abs topbar-social">
  <svg viewBox="0 0 20 20"><circle cx="10" cy="10" r="8.5" fill="none" stroke="#fff" stroke-width="1.5"/><circle cx="7" cy="10" r="1.6" fill="#fff"/><circle cx="13" cy="6.5" r="1.6" fill="#fff"/><circle cx="13" cy="13.5" r="1.6" fill="#fff"/><path d="M7 10l6-3.5M7 10l6 3.5" stroke="#fff" stroke-width="1"/></svg>
  <svg viewBox="0 0 20 20"><circle cx="10" cy="10" r="8.5" fill="none" stroke="#fff" stroke-width="1.5"/><rect x="5" y="7" width="10" height="7" fill="none" stroke="#fff" stroke-width="1.3"/><path d="M5 7l5 4 5-4" fill="none" stroke="#fff" stroke-width="1.3"/></svg>
  <svg viewBox="0 0 20 20"><circle cx="10" cy="10" r="8.5" fill="none" stroke="#fff" stroke-width="1.5"/><circle cx="10" cy="10" r="4.5" fill="none" stroke="#fff" stroke-width="1.2"/><path d="M5.5 10h9M10 5.5v9" stroke="#fff" stroke-width="1"/></svg>
  <svg viewBox="0 0 20 20"><circle cx="10" cy="10" r="8.5" fill="none" stroke="#fff" stroke-width="1.5"/><path d="M8 12l4-4M7 10l-1 1a2 2 0 003 3l1-1M13 10l1-1a2 2 0 00-3-3l-1 1" fill="none" stroke="#fff" stroke-width="1.3"/></svg>
</div>

<div class="abs header"></div>
<div class="abs brand" style="left:111px;top:85px"><span class="brand-dot"></span><span>The K7 Momentum<br>Collective</span></div>
<nav class="abs nav">
  <span class="active">HOME</span><span>ABOUT US</span><span>SERVICES</span><span>RESOURCES</span><span>CONTACT US</span><span>|</span>
  <svg width="14" height="14" viewBox="0 0 24 24"><circle cx="10" cy="10" r="7" stroke="#222" stroke-width="3" fill="none"/><path d="M15 15l7 7" stroke="#222" stroke-width="3"/></svg>
</nav>

<section class="abs hero">
  <div class="hero-photo" role="img" aria-label="Photo of a business team shaking hands around a meeting table"></div>
  <svg class="abs" style="left:0;top:0" width="1200" height="650" viewBox="0 0 1200 650">
    <path d="M0 447 Q600 799 1200 447 L1200 650 L0 650 Z" fill="#fff"/>
    <path d="M105 505 Q600 793 1095 505 Q600 762 105 505 Z" fill="var(--blue)"/>
  </svg>
  <div class="abs hero-box">
    <h1>THE K7 MOMENTUM COLLECTIVE</h1>
    <p>The K7 Momentum Collective (K7) is a group of experienced executives whose careers have been focused</p>
    <span class="btn">GET STARTED</span>
  </div>
</section>

<div class="abs about-img"><div role="img" aria-label="Photo of professionals shaking hands across an office desk"></div></div>
<div class="abs about-text">
  <div class="h2"><span class="b">ABOUT</span> <span class="g">US</span></div>
  <p>The K7 Momentum Collective (K7) is a group of experienced executives whose careers have been focused on taking innovative ideas to market by strategically navigating the buildout of best-in-class life science and diagnostic organizations. This experience makes us uniquely equipped to be involved in all aspects of your due diligence on new or existing investments (business analysis, industry thesis, competitive landscape, business/pricing model, and financial modeling as it relates to validation of the assumptions in the model to determine the return expectations). This includes the following services:</p>
  <span class="btn">LEARN MORE</span>
</div>

<section class="abs solution">
  <h2>OUR SOLUTION</h2>
  <div class="abs sol-card" style="left:111px"><svg class="ic" viewBox="0 0 114 114"><circle cx="57" cy="57" r="57" fill="#8a8a8a"/><circle cx="57" cy="57" r="47" fill="none" stroke="#fff" stroke-width="1.5" stroke-dasharray="5 4"/><rect x="39" y="38" width="36" height="28" rx="2" fill="none" stroke="#fff" stroke-width="2.5"/><path d="M39 45h36M44 52h14M44 58h10M50 76h14M57 66v10" stroke="#fff" stroke-width="2.5"/><rect x="62" y="51" width="8" height="9" fill="none" stroke="#fff" stroke-width="2"/></svg><span>DISCOVERY</span></div>
  <div class="abs sol-card" style="left:360px"><svg class="ic" viewBox="0 0 114 114"><circle cx="57" cy="57" r="57" fill="#8a8a8a"/><circle cx="57" cy="57" r="47" fill="none" stroke="#fff" stroke-width="1.5" stroke-dasharray="5 4"/><path d="M57 36a15 15 0 00-9 27v6h18v-6a15 15 0 00-9-27z" fill="none" stroke="#fff" stroke-width="2.5"/><path d="M51 74h12M53 79h8M57 46v10M52 51h10" stroke="#fff" stroke-width="2.5"/></svg><span>INNOVATIVE IP</span></div>
  <div class="abs sol-card on" style="left:609px"><svg class="ic" viewBox="0 0 114 114"><circle cx="57" cy="57" r="57" fill="var(--blue)"/><circle cx="57" cy="57" r="47" fill="none" stroke="#fff" stroke-width="1.5" stroke-dasharray="5 4"/><rect x="36" y="38" width="42" height="30" fill="none" stroke="#fff" stroke-width="2.5"/><path d="M43 62v-6M50 62v-10M57 62v-4M50 68l-6 10M64 68l6 10M57 34v4" stroke="#fff" stroke-width="2.5"/><circle cx="67" cy="51" r="5" fill="none" stroke="#fff" stroke-width="2.2"/><path d="M71 55l4 4" stroke="#fff" stroke-width="2.2"/></svg><span>STRATEGIC<br>BUSINESS PLAN</span></div>
  <div class="abs sol-card" style="left:857px"><svg class="ic" viewBox="0 0 114 114"><circle cx="57" cy="57" r="57" fill="#8a8a8a"/><circle cx="57" cy="57" r="47" fill="none" stroke="#fff" stroke-width="1.5" stroke-dasharray="5 4"/><rect x="50" y="54" width="14" height="24" fill="none" stroke="#fff" stroke-width="2.5"/><path d="M54 60h6M54 66h6M54 72h6M40 78v-10M74 78v-10M36 78h42" stroke="#fff" stroke-width="2.2"/><circle cx="44" cy="42" r="4" fill="none" stroke="#fff" stroke-width="2"/><circle cx="57" cy="38" r="4" fill="none" stroke="#fff" stroke-width="2"/><circle cx="70" cy="42" r="4" fill="none" stroke="#fff" stroke-width="2"/></svg><span>COMPANY<br>FORMATION</span></div>
</section>

<div class="abs team-h"><span style="color:var(--blue)">MEET</span><br><span style="color:var(--grey)">OUR TEAM</span></div>
<div class="abs member" style="left:337px"><div class="ph" role="img" aria-label="Portrait of team member Maren Holt"></div><div class="tag">MAREN HOLT</div></div>
<div class="abs member on" style="left:598px"><div class="ph" role="img" aria-label="Portrait of team member Dana Ruiz"></div><div class="tag">DANA RUIZ</div></div>
<div class="abs member" style="left:861px"><div class="ph" role="img" aria-label="Portrait of team member Lena Ostrov"></div><div class="tag">LENA OSTROV</div></div>

<section class="abs plan">
  <h2>K7 PLAN ELEMENTS</h2>
  <div class="abs plan-card" style="left:111px"><svg class="ic" viewBox="0 0 90 90"><circle cx="45" cy="45" r="45" fill="#8a8a8a"/><circle cx="45" cy="30" r="6" fill="none" stroke="#fff" stroke-width="2.2"/><path d="M36 46a9 9 0 0118 0M45 46v6M30 52h30M30 52v5M40 52v5M50 52v5M60 52v5" fill="none" stroke="#fff" stroke-width="2.2"/><circle cx="30" cy="61" r="3" fill="none" stroke="#fff" stroke-width="2"/><circle cx="40" cy="61" r="3" fill="none" stroke="#fff" stroke-width="2"/><circle cx="50" cy="61" r="3" fill="none" stroke="#fff" stroke-width="2"/><circle cx="60" cy="61" r="3" fill="none" stroke="#fff" stroke-width="2"/></svg><h3>EXECUTIVE SUMMARY</h3><p>Articulates a brief snapshot of the business model/plan, including name, location, products or services, mission statement, and organizational values/ cultural beliefs.</p></div>
  <div class="abs plan-card on" style="left:447px"><svg class="ic" viewBox="0 0 90 90"><circle cx="45" cy="45" r="45" fill="var(--blue)"/><rect x="30" y="25" width="28" height="40" rx="2" fill="none" stroke="#fff" stroke-width="2.2"/><rect x="38" y="21" width="12" height="7" rx="1.5" fill="var(--blue)" stroke="#fff" stroke-width="2"/><path d="M35 36l2 2 3-4M43 36h10M35 45l2 2 3-4M43 45h10M35 54l2 2 3-4M43 54h8" fill="none" stroke="#fff" stroke-width="2"/><circle cx="60" cy="60" r="7" fill="var(--blue)" stroke="#fff" stroke-width="2"/><circle cx="60" cy="60" r="2.5" fill="#fff"/></svg><h3>COMPANY DESCRIPTION</h3><p>Describes a high-level view of the business nature, customer need being met, history, legality, short term, and long-term goals.</p></div>
  <div class="abs plan-card" style="left:783px"><svg class="ic" viewBox="0 0 90 90"><circle cx="45" cy="45" r="45" fill="#8a8a8a"/><rect x="26" y="28" width="34" height="28" fill="none" stroke="#fff" stroke-width="2.2"/><path d="M32 50v-6M38 50v-10M44 50v-4M30 40l8-6 6 4 10-8" fill="none" stroke="#fff" stroke-width="2"/><circle cx="59" cy="57" r="8" fill="#8a8a8a" stroke="#fff" stroke-width="2.2"/><path d="M65 63l5 5" stroke="#fff" stroke-width="2.5"/><path d="M55 57h8M59 53v8" stroke="#fff" stroke-width="1.6"/></svg><h3>MARKET ANALYSIS</h3><p>Displays research and plan to reach the target demographic as well as the size, direction, and competitors in the overall industry.</p></div>
  <div class="abs dots"><i></i><i class="on"></i><i></i><i></i></div>
</section>

<div class="abs touch-h h2"><span class="b">GET IN</span> <span class="g">TOUCH</span></div>
<div class="abs field" style="left:235px;top:3178px;width:360px">First Name</div>
<div class="abs field" style="left:605px;top:3178px;width:360px">Last Name</div>
<div class="abs field" style="left:235px;top:3241px;width:360px">Phone Number</div>
<div class="abs field" style="left:605px;top:3241px;width:360px">Email Address</div>
<div class="abs field" style="left:235px;top:3303px;width:730px;height:94px">Message</div>
<span class="abs btn" style="left:527px;top:3408px;width:145px;height:48px;line-height:48px;text-align:center;padding:0">SUBMIT NOW</span>

<footer class="abs footer">
  <div class="brand"><span class="brand-dot"></span><span>The K7 Momentum<br>Collective</span></div>
  <div class="fnav"><span>HOME</span><span>|</span><span>ABOUT US</span><span>|</span><span>SERVICES</span><span>|</span><span>RESOURCES</span><span>|</span><span>CONTACT US</span></div>
  <div class="fcontact"><span style="color:var(--blue)">&#9990;</span> +1 (555) 014 7720 &nbsp; | &nbsp; <span style="color:var(--blue)">&#9993;</span> hello@k7momentumcollective.com</div>
  <div class="fsocial">
    <svg viewBox="0 0 33 33"><circle cx="16.5" cy="16.5" r="16.5" fill="var(--blue)"/><circle cx="12" cy="16.5" r="2.3" fill="#fff"/><circle cx="21" cy="11" r="2.3" fill="#fff"/><circle cx="21" cy="22" r="2.3" fill="#fff"/><path d="M12 16.5l9-5.5M12 16.5l9 5.5" stroke="#fff" stroke-width="1.4"/></svg>
    <svg viewBox="0 0 33 33"><circle cx="16.5" cy="16.5" r="16.5" fill="#fff"/><rect x="9" y="11" width="15" height="11" fill="none" stroke="#222" stroke-width="1.8"/><path d="M9 11l7.5 6 7.5-6" fill="none" stroke="#222" stroke-width="1.8"/></svg>
    <svg viewBox="0 0 33 33"><circle cx="16.5" cy="16.5" r="16.5" fill="#fff"/><circle cx="16.5" cy="16.5" r="7" fill="none" stroke="#222" stroke-width="1.8"/><path d="M9.5 16.5h14M16.5 9.5v14" stroke="#222" stroke-width="1.4"/></svg>
    <svg viewBox="0 0 33 33"><circle cx="16.5" cy="16.5" r="16.5" fill="#fff"/><path d="M14 19l5-5M12.5 16.5l-1.5 1.5a3 3 0 004 4l1.5-1.5M20.5 16.5l1.5-1.5a3 3 0 00-4-4l-1.5 1.5" fill="none" stroke="#222" stroke-width="1.8"/></svg>
  </div>
  <div class="fline"></div>
  <div class="fcopy">© 2023 <b>THE K7 MOMENTUM COLLECTIVE</b> &nbsp;|&nbsp; All Rights Reserved</div>
</footer>

</body>
</html>
```